Kelvar Systems Sdn. Bhd. - logo/ B.Card and letter head
Kelvar Systems Sdn. Bhd.
Kelvar Systems Sdn. Bhd. - logo/ B.Card and letter head - Information Technology
Creative Brief
Professional
Daniel Loh
Director
Lot B14, Second Floor, East Block Meridian Shopping Mall, Jalan Cempaka 7/3, Taman Sri Kenari, 43200 Cheras, Selangor D.E
daniel.loh@kelvarplay.com
512863 - P
The name and designation will be updated later. Please include the font type on on the design upon confirmation of the design. KVS is Information technology which is specilaise in lottery and gaming business so the designer will think a logo for us. You need to specific to the designer that you need a logo
will be updated later when everything had been finalized.

```html
<!DOCTYPE html>
<html lang="en">
<head>
<meta charset="utf-8">
<title>Kelvar Systems Sdn. Bhd. – Business Cards</title>
<link href="https://fonts.googleapis.com/css2?family=Arimo:wght@400;700&family=Roboto+Condensed:wght@700&display=swap" rel="stylesheet">
<style>
  :root {
    --backdrop: #e9e9e9;
    --card-dark: #000000;
    --card-light: #ffffff;
    --ink-dark: #1a1a1a;
    --ink-light: #ffffff;
    --ink-muted-dark: #4a4a4a;
    --ink-muted-light: #e6e6e6;
  }
  * { box-sizing: border-box; margin: 0; padding: 0; }
  html, body {
    width: 1200px; height: 883px; overflow: hidden;
    background: var(--backdrop);
  }
  .canvas { position: relative; width: 1200px; height: 883px; }
  .card {
    position: absolute; top: 230px; width: 283px; height: 470px;
    font-family: "Arimo", Arial, sans-serif;
    text-align: center;
    box-shadow: 0 2px 8px rgba(0,0,0,0.15);
  }
  .card--dark { left: 125px; background: var(--card-dark); color: var(--ink-light); }
  .card--light { left: 480px; background: var(--card-light); color: var(--ink-dark); }

  .brand { position: absolute; left: 66px; top: 42px; text-align: left; }
  .brand-name {
    font-family: "Arimo", Arial, sans-serif;
    font-weight: 700; font-size: 40px; line-height: 1;
    letter-spacing: 1px;
  }
  .brand-legal {
    font-family: "Arimo", Arial, sans-serif;
    font-weight: 700; font-size: 11px; margin-top: 8px;
  }

  .person { position: absolute; left: 0; right: 0; top: 205px; }
  .person-name {
    font-family: "Roboto Condensed", "Arial Narrow", sans-serif;
    font-weight: 700; font-size: 28px; line-height: 1.1;
  }
  .person-role { font-size: 13px; margin-top: 4px; }

  .address, .contact {
    position: absolute; left: 0; right: 0;
    font-size: 13px; line-height: 18px; font-style: normal;
  }
  .address { top: 283px; }
  .contact { top: 400px; }
  .card--dark .address, .card--dark .contact { color: var(--ink-muted-light); }
  .card--light .address, .card--light .contact { color: var(--ink-muted-dark); }
</style>
</head>
<body>
<main class="canvas">

  <article class="card card--dark">
    <header class="brand">
      <div class="brand-name">KVS</div>
      <div class="brand-legal">Kelvar Systems Sdn. Bhd.</div>
    </header>
    <section class="person">
      <h1 class="person-name">Daniel Loh</h1>
      <p class="person-role">Director</p>
    </section>
    <address class="address">
      Lot B14, Second Floor,<br>
      East Block Meridian Shopping Mall,<br>
      Jalan Cempaka 7/3,<br>
      Taman Sri Kenari,<br>
      43200 Cheras,<br>
      Selangor D.E
    </address>
    <p class="contact">
      Phone&nbsp; 03 - 5812 4407<br>
      Fax&nbsp; 03 - 5812 4419<br>
      daniel.loh@kelvarplay.com
    </p>
  </article>

  <article class="card card--light">
    <header class="brand">
      <div class="brand-name">KVS</div>
      <div class="brand-legal">Kelvar Systems Sdn. Bhd.</div>
    </header>
    <section class="person">
      <h1 class="person-name">Daniel Loh</h1>
      <p class="person-role">Director</p>
    </section>
    <address class="address">
      Lot B14, Second Floor,<br>
      East Block Meridian Shopping Mall,<br>
      Jalan Cempaka 7/3,<br>
      Taman Sri Kenari,<br>
      43200 Cheras,<br>
      Selangor D.E
    </address>
    <p class="contact">
      Phone&nbsp; 03 - 5812 4407<br>
      Fax&nbsp; 03 - 5812 4419<br>
      daniel.loh@kelvarplay.com
    </p>
  </article>

</main>
</body>
</html>
```